Redesign of Business Card to look more professional and stand out

Business card design. You can lean more about our company by going to dkrfabworks.example. Raised letters would be nice. Company name & Address
DK&R
418 Wendlow Ridge Drive, Suite 340
Marbury Springs, KY 40611

You can use my name and title: Glenn Harwick
Business Development Manager

Target Market(s)

Heavy Industrial market, i.e. utilities, chemical plants, paper mills, construction companies

Industry/Entity Type

Construction

Contact Information for Business Card

We provide Project Management & Project Support Services

Font styles to use
Serif

Requirements
Must have
• Company name & Address
• DK&R
• 418 Wendlow Ridge Drive, Suite 340
• Marbury Springs, KY 40611
Nice to have
• ideas for the back of the card
Should not have
• no crazy colors. needs to look professional and standout.

```html
<!DOCTYPE html>
<html lang="en">
<head>
<meta charset="utf-8">
<title>DK&amp;R Business Card</title>
<link rel="stylesheet" href="https://fonts.googleapis.com/css2?family=PT+Serif:wght@400;700&display=swap">
<style>
  :root {
    --navy: #1f3666;
    --navy-deep: #1b3262;
    --mist: #dcdce6;
    --lilac: #6a6d93;
    --paper: #ffffff;
    --backdrop: #e6e7eb;
    --rule: #9aa3b8;
  }
  * { margin: 0; padding: 0; box-sizing: border-box; }
  html, body {
    width: 1200px; height: 900px; overflow: hidden;
    background: var(--backdrop);
    font-family: "PT Serif", Georgia, serif;
  }
  .canvas { position: relative; width: 1200px; height: 900px; }
  .card {
    position: absolute;
    width: 680px; height: 389px;
    border-radius: 22px;
    box-shadow: 0 10px 28px rgba(20, 28, 50, 0.22);
    overflow: hidden;
  }
  .card--front {
    left: 150px; top: 48px;
    background: linear-gradient(100deg, var(--mist) 0%, var(--lilac) 38%, #3a4a7a 68%, var(--navy-deep) 100%);
    display: flex; align-items: center; justify-content: center;
  }
  .card--back {
    left: 370px; top: 463px;
    background: var(--paper);
  }
  .brand-name {
    font-family: "PT Serif", Georgia, serif;
    font-weight: 700;
    letter-spacing: 2px;
    line-height: 1;
    white-space: nowrap;
  }
  .card--front .brand-name { color: var(--paper); font-size: 150px; }
  .card--back .brand-name {
    position: absolute; left: 44px; top: 168px;
    color: var(--navy); font-size: 92px;
  }
  .divider {
    position: absolute; left: 384px; top: 92px;
    width: 1px; height: 150px; background: var(--rule);
  }
  .contact {
    position: absolute; left: 400px; top: 92px;
    color: var(--navy);
    white-space: nowrap;
  }
  .contact__name {
    font-weight: 700; font-size: 22px; letter-spacing: 0.5px;
    text-transform: uppercase; line-height: 1.1;
  }
  .contact__title { font-size: 14px; margin-bottom: 8px; line-height: 1.3; }
  .contact__line { font-size: 14px; line-height: 1.35; display: flex; align-items: center; gap: 6px; }
  .contact__line svg { width: 12px; height: 12px; flex: none; }
  .contact__address { margin-bottom: 4px; }
</style>
</head>
<body>
<main class="canvas">
  <section class="card card--front" aria-label="Card front">
    <div class="brand-name">DK&amp;R</div>
  </section>

  <section class="card card--back" aria-label="Card back">
    <div class="brand-name">DK&amp;R</div>
    <div class="divider"></div>
    <div class="contact">
      <div class="contact__name">Glenn Harwick</div>
      <div class="contact__title">Business Development Manager</div>
      <div class="contact__address">
        <div class="contact__line">418 Wendlow Ridge Drive</div>
        <div class="contact__line">Suite 340 Marbury Springs, KY 40611</div>
      </div>
      <div class="contact__line">
        <svg viewBox="0 0 24 24" aria-hidden="true"><path fill="#1f3666" d="M6.6 10.8a15.1 15.1 0 0 0 6.6 6.6l2.2-2.2c.3-.3.7-.4 1-.2 1.1.4 2.3.6 3.6.6.6 0 1 .4 1 1V20c0 .6-.4 1-1 1A17 17 0 0 1 3 4c0-.6.4-1 1-1h3.5c.6 0 1 .4 1 1 0 1.3.2 2.5.6 3.6.1.3 0 .7-.2 1z"/></svg>
        614.555.0148
      </div>
      <div class="contact__line">
        <svg viewBox="0 0 24 24" aria-hidden="true"><rect x="3" y="5" width="18" height="14" rx="1.5" fill="none" stroke="#1f3666" stroke-width="2"/><path d="M3.5 6l8.5 7 8.5-7" fill="none" stroke="#1f3666" stroke-width="2"/></svg>
        gharwick@dkr-fieldops.example
      </div>
    </div>
  </section>
</main>
</body>
</html>
```